Kestrel Electrical Business Card

We need a business card design for our family-run electrical contracting business based in Western Australia called 'Kestrel Electrical'. We provide electrical services including residential, commercial and industrial. We aim for individual business cards to be made for all of our employees. We already have a company logo, which we require to be featured on the design. We would like simple, sleek and vibrant designs, which incorporate our logo and represent our business. We do not want anything involving too many graphics/images. We like the colours red, black, white and all shades of grey. The final design should communicate professionalism and trustworthiness.
We require the following contact information:
Name- Owen Strickland
EC 5809
Mobile number- 0455 918 302
Fax number (including area code)- (08) 9640 2718
Email adress- name@kestrelelectrical.example
Electrical
- ITC Handel Bold

```html
<!DOCTYPE html>
<html lang="en">
<head>
<meta charset="utf-8">
<title>Kestrel Electrical Business Card</title>
<link rel="stylesheet" href="https://fonts.googleapis.com/css2?family=Oswald:wght@600&family=Open+Sans:wght@400;600;700&display=swap">
<style>
  :root {
    --backdrop: #e4e4e4;
    --card: #ffffff;
    --card-edge: #f1f1f1;
    --charcoal: #3a3a3c;
    --ink: #262626;
    --red: #e3161b;
    --panel-text: #ffffff;
  }
  * { margin: 0; padding: 0; box-sizing: border-box; }
  html, body {
    width: 1200px; height: 900px; overflow: hidden;
    background: var(--backdrop);
  }
  .card {
    position: absolute; left: 100px; top: 164px;
    width: 1000px; height: 572px;
    background: linear-gradient(135deg, var(--card) 0%, var(--card-edge) 100%);
    box-shadow: 0 18px 40px rgba(0,0,0,0.18);
    overflow: hidden;
  }
  .card__panel { position: absolute; inset: 0; width: 1000px; height: 572px; }
  .brand {
    position: absolute; left: 70px; top: 220px;
    display: flex; align-items: center; gap: 16px;
  }
  .brand__mark { width: 40px; height: 40px; background: var(--red); }
  .brand__name {
    font-family: "Open Sans", sans-serif; font-weight: 700;
    font-size: 36px; letter-spacing: 0.5px; color: var(--ink);
    text-transform: uppercase;
  }
  .person {
    position: absolute; left: 70px; top: 420px;
  }
  .person__name {
    font-family: "Oswald", sans-serif; font-weight: 600;
    font-size: 42px; line-height: 1; color: var(--red);
    text-transform: uppercase; letter-spacing: 0.5px;
  }
  .person__role {
    margin-top: 8px;
    font-family: "Open Sans", sans-serif; font-weight: 700;
    font-size: 17px; color: var(--ink); text-transform: uppercase;
    letter-spacing: 0.5px;
  }
  .contacts {
    position: absolute; right: 40px; top: 90px;
    list-style: none;
    font-family: "Open Sans", sans-serif; font-weight: 400;
    font-size: 17px; color: var(--panel-text);
  }
  .contacts li {
    display: flex; justify-content: flex-end; align-items: center;
    gap: 12px; height: 38px;
  }
  .contacts svg { width: 18px; height: 18px; flex: none; }
</style>
</head>
<body>
  <div class="card">
    <svg class="card__panel" viewBox="0 0 1000 572" aria-hidden="true">
      <path d="M600 0 L1000 0 L1000 572 L468 572 C548 420 592 220 600 0 Z" fill="var(--red)"/>
      <path d="M630 0 L1000 0 L1000 572 L490 572 C570 420 620 220 630 0 Z" fill="var(--charcoal)"/>
    </svg>

    <div class="brand">
      <span class="brand__mark"></span>
      <span class="brand__name">Kestrel Electrical</span>
    </div>

    <div class="person">
      <div class="person__name">Owen Strickland</div>
      <div class="person__role">Electrical Contractor · EC 5809</div>
    </div>

    <ul class="contacts">
      <li>0455 918 302
        <svg viewBox="0 0 20 20"><rect x="5" y="1.5" width="10" height="17" rx="2" fill="none" stroke="#fff" stroke-width="1.6"/><circle cx="10" cy="15.5" r="1" fill="#fff"/></svg>
      </li>
      <li>(08) 9640 2718
        <svg viewBox="0 0 20 20"><path d="M5 2 L8 6 L6.5 8 C7.5 10.5 9.5 12.5 12 13.5 L14 12 L18 15 L16 18 C9 18 2 11 2 4 Z" fill="#fff"/></svg>
      </li>
      <li>name@kestrelelectrical.example
        <svg viewBox="0 0 20 20"><rect x="2" y="4" width="16" height="12" fill="#fff"/><path d="M2 4 L10 11 L18 4" fill="none" stroke="var(--charcoal)" stroke-width="1.4"/></svg>
      </li>
      <li>www.kestrelelectrical.example
        <svg viewBox="0 0 20 20"><circle cx="10" cy="10" r="8" fill="none" stroke="#fff" stroke-width="1.5"/><ellipse cx="10" cy="10" rx="3.5" ry="8" fill="none" stroke="#fff" stroke-width="1.2"/><path d="M2 10 H18 M3.5 6 H16.5 M3.5 14 H16.5" stroke="#fff" stroke-width="1.2"/></svg>
      </li>
      <li>27 Osprey Way, Malaga WA 6090
        <svg viewBox="0 0 20 20"><path d="M10 1.5 C6 1.5 3.5 4.5 3.5 8 C3.5 12.5 10 18.5 10 18.5 C10 18.5 16.5 12.5 16.5 8 C16.5 4.5 14 1.5 10 1.5 Z" fill="#fff"/><circle cx="10" cy="8" r="2.5" fill="var(--charcoal)"/></svg>
      </li>
    </ul>
  </div>
</body>
</html>
```